Cosmetic Dentist Practice needs stationery package/logo

I need a letterhead, envelope and business card for a cosmetic and Dental Inplant practice in an upscale part of Houston. The business card will be a size 3.5 x 2 and the letterhead will be 8.5" x 11" with a standard #10 envelope.
I have uploaded a file with an idea that the dentist had for his cards. Please note that this is not the size that the card should be. It does provide the information required.
Updates
Thank you all for your submissions. They were each unique and special in their own way. My client has made a selection that he feels best meets his needs. I appreciate each of you taking the time to offer designs. Good luck to each of you...I hope to see you back in MarblePost on future projects.
Industry/Entity Type
Business
Look and feel
Each slider illustrates characteristics of the customer's brand and the style your logo design should communicate.

```html
<!DOCTYPE html>
<html lang="en">
<head>
<meta charset="utf-8">
<title>Linden Cosmetic and Implant Dentistry – Stationery</title>
<link rel="stylesheet" href="https://fonts.googleapis.com/css2?family=Open+Sans:wght@300;400;700&display=swap">
<style>
  :root{
    --backdrop:#e6e6e6;
    --paper:#ffffff;
    --brand-blue:#00aeef;
    --brand-blue-soft:#7fd3f5;
    --panel-grey:#d1d3d5;
    --panel-grey-soft:#e8e9eb;
    --mark-grey:#bcbec0;
    --text-grey:#9a9b9d;
    --text-dark:#58595b;
    --rule-grey:#c9cacc;
  }
  *{margin:0;padding:0;box-sizing:border-box}
  html,body{width:1200px;height:1000px;overflow:hidden;background:var(--backdrop);font-family:"Open Sans",Arial,sans-serif}
  .canvas{position:relative;width:1200px;height:1000px}

  /* Envelope */
  .envelope{position:absolute;left:88px;top:105px;width:1025px;height:445px;background:var(--paper);overflow:hidden;box-shadow:0 4px 22px rgba(90,110,110,.35)}
  .envelope__sweep{position:absolute;inset:0}
  .envelope__mark{position:absolute;left:38px;top:38px;width:80px;height:80px;border-radius:50%;background:var(--mark-grey)}
  .envelope__name{position:absolute;left:128px;top:46px;font-weight:300;font-size:40px;line-height:1;color:var(--brand-blue);letter-spacing:1px}
  .envelope__tagline{position:absolute;left:132px;top:89px;font-size:10.5px;color:var(--text-grey)}
  .envelope__address{position:absolute;left:38px;top:137px;font-weight:300;font-size:16.5px;line-height:20px;color:var(--text-grey)}

  /* Appointment card */
  .card{position:absolute;left:385px;top:679px;width:432px;height:215px;background:var(--paper);overflow:hidden;box-shadow:0 4px 20px rgba(90,110,110,.35)}
  .card__sweep{position:absolute;inset:0}
  .card__mark{position:absolute;left:23px;top:138px;width:52px;height:52px;border-radius:50%;background:var(--mark-grey)}
  .card__brand{position:absolute;left:30px;top:128px;transform:rotate(-90deg);transform-origin:0 0;white-space:nowrap}
  .card__name{display:block;font-weight:300;font-size:27px;line-height:1;color:var(--brand-blue);letter-spacing:.5px}
  .card__tagline{display:block;font-size:7px;color:var(--text-grey);margin-top:2px}
  .card__notice{position:absolute;left:86px;top:22px;font-size:11px;color:var(--text-dark)}
  .card__notice strong{color:var(--brand-blue);font-weight:700}
  .schedule{position:absolute;left:86px;top:43px;width:324px;border-collapse:collapse;font-size:11px;color:var(--text-dark)}
  .schedule th{font-weight:400;height:18px;text-align:center}
  .schedule td{border:1px solid var(--rule-grey);height:26px}
  .schedule .col-date{width:104px}
  .schedule .col-day{width:115px}
</style>
</head>
<body>
<main class="canvas">

  <section class="envelope" aria-label="#10 envelope">
    <svg class="envelope__sweep" width="1025" height="445" viewBox="0 0 1025 445" aria-hidden="true">
      <path d="M812 0 C805 200 700 370 492 445 L1025 445 L1025 0 Z" fill="var(--panel-grey)"/>
      <path d="M812 0 C805 200 700 370 492 445" fill="none" stroke="var(--brand-blue)" stroke-width="8"/>
    </svg>
    <div class="envelope__mark"></div>
    <div class="envelope__name">LINDEN</div>
    <div class="envelope__tagline">Cosmetic and Implant Dentistry</div>
    <address class="envelope__address" style="font-style:normal">84 Cedar Ridge Lane Suite 210 W.<br>Houston, TX. 77019</address>
  </section>

  <section class="card" aria-label="Appointment card">
    <svg class="card__sweep" width="432" height="215" viewBox="0 0 432 215" aria-hidden="true">
      <path d="M410 0 C410 90 370 175 260 215 L432 215 L432 0 Z" fill="var(--panel-grey-soft)"/>
    </svg>
    <div class="card__mark"></div>
    <div class="card__brand">
      <span class="card__name">LINDEN</span>
      <span class="card__tagline">Cosmetic and Implant Dentistry</span>
    </div>
    <p class="card__notice">If unable to keep appointment, kindly give <strong>24 hrs.</strong> notice</p>
    <table class="schedule">
      <thead><tr><th class="col-date">Date</th><th class="col-day">Day</th><th>Time</th></tr></thead>
      <tbody>
        <tr><td></td><td></td><td></td></tr>
        <tr><td></td><td></td><td></td></tr>
        <tr><td></td><td></td><td></td></tr>
        <tr><td></td><td></td><td></td></tr>
        <tr><td></td><td></td><td></td></tr>
      </tbody>
    </table>
    <svg class="card__sweep" width="432" height="215" viewBox="0 0 432 215" aria-hidden="true">
      <path d="M410 0 C410 90 370 175 260 215" fill="none" stroke="var(--brand-blue-soft)" stroke-width="2.5"/>
    </svg>
  </section>

</main>
</body>
</html>
```